Box Design for Flooring product

***IMPORTANT: PLEASE READ THE DOCUMENT PROVIDED WITH THIS BRIEF CAREFULLY BEFORE ACCEPTING THIS PROJECT***
Need a creative design for the packaging of a flooring product. The packaging is two boxes: one holding 36 planks of flooring, and the other 7 planks of flooring. There are 4 colours for the flooring planks that need a box designed (for both the 36 plank box and 7 plank box). The boxes measures 92 cm x 16cm x 7cm (36 planks) and 92 cm x 16cm x 1.5cm (7 planks).
More details are provided in the requirements document attached with this brief. Also attaching other supporting documents with this brief mentioned in the document.
Need extra days to review
- Montserrat-Regular

```html
<!DOCTYPE html>
<html lang="en">
<head>
<meta charset="utf-8">
<title>Self Adhesive Vinyl Planks – Box Panel</title>
<link href="https://fonts.googleapis.com/css2?family=Fira+Sans:wght@300;400&family=Barlow:wght@400;500;600&family=Montserrat:wght@400;500&display=swap" rel="stylesheet">
<style>
  :root {
    --bg: #b1b0ae;
    --brown: #5e5446;
    --taupe: #a39b90;
    --band: #cfcbc5;
    --white: #ffffff;
    --wall: #ebe8e3;
    --door: #e6e3de;
    --wood-light: #e2c596;
    --wood-dark: #c89e6b;
  }
  html, body {
    margin: 0;
    width: 1200px;
    height: 703px;
    overflow: hidden;
    background: var(--bg);
  }
  .box-panel {
    position: absolute;
    left: 101px;
    top: 270px;
    width: 986px;
    height: 172px;
    display: block;
  }
  .title-main { font-family: "Fira Sans", sans-serif; font-weight: 300; fill: var(--white); }
  .title-sub { font-family: "Fira Sans", sans-serif; font-weight: 400; fill: var(--brown); }
  .spec-text { font-family: "Barlow", sans-serif; font-weight: 400; }
  .spec-dark { fill: var(--brown); }
  .spec-light { fill: var(--white); }
  .feature-label { font-family: "Barlow", sans-serif; font-weight: 400; fill: var(--white); }
  .room-label { font-family: "Barlow", sans-serif; font-weight: 500; fill: var(--white); }
  .use-label { font-family: "Barlow", sans-serif; font-weight: 400; fill: var(--brown); }
  .brand-name { font-family: "Montserrat", sans-serif; font-weight: 500; fill: var(--brown); letter-spacing: 1px; }
  .brand-tagline { font-family: "Montserrat", sans-serif; font-weight: 500; fill: var(--brown); letter-spacing: 1px; }
  .icon-line { fill: none; stroke: var(--white); stroke-width: 2.5; stroke-linecap: round; stroke-linejoin: round; }
  .icon-fill { fill: var(--white); }
</style>
</head>
<body>
<svg class="box-panel" viewBox="0 0 1644 286" xmlns="http://www.w3.org/2000/svg">
  <defs>
    <linearGradient id="room-floor" x1="0" y1="0" x2="0" y2="1">
      <stop offset="0" stop-color="var(--wall)"/>
      <stop offset="0.2" stop-color="var(--wall)"/>
      <stop offset="0.26" stop-color="var(--wood-light)"/>
      <stop offset="1" stop-color="var(--wood-dark)"/>
    </linearGradient>
    <linearGradient id="room-door" x1="0" y1="0" x2="1" y2="0">
      <stop offset="0" stop-color="var(--door)" stop-opacity="1"/>
      <stop offset="0.26" stop-color="var(--door)" stop-opacity="0.9"/>
      <stop offset="0.34" stop-color="var(--door)" stop-opacity="0"/>
      <stop offset="1" stop-color="var(--door)" stop-opacity="0"/>
    </linearGradient>
  </defs>

  <g role="img" aria-label="Photo of a room with light oak vinyl plank flooring, white skirting and an open white door">
    <rect x="829" y="0" width="815" height="286" fill="url(#room-floor)"/>
    <rect x="829" y="0" width="815" height="286" fill="url(#room-door)"/>
  </g>

  <rect x="397" y="0" width="432" height="286" fill="var(--taupe)"/>
  <polygon points="0,0 962,0 397,286 0,286" fill="var(--brown)"/>

  <polygon points="0,30 342,30 300,75 0,75" fill="var(--band)"/>
  <text class="title-sub" x="50" y="67" font-size="40">Self Adhesive</text>

  <polygon points="378,16 872,16 872,50 342,50" fill="var(--band)"/>
  <text class="spec-text spec-dark" x="392" y="42" font-size="23">Pack coverage 5m²(36 per planks pack)</text>
  <text class="spec-text spec-light" x="390" y="76" font-size="19">Plank size 914mm x 152mm (36” x 6” approx.)</text>

  <text class="title-main" x="44" y="167" font-size="104">Vinyl Planks</text>

  <g class="feature easy-lay">
    <path class="icon-line" d="M40,238 L62,216 L114,216 L120,238 Z M56,238 L72,216 M76,238 L88,216 M96,238 L102,216"/>
    <circle class="icon-fill" cx="86" cy="221" r="5"/>
    <path class="icon-line" d="M74,232 L86,226 L96,232"/>
    <text class="feature-label" x="79" y="266" font-size="16.5" text-anchor="middle">Easy to lay</text>
  </g>
  <g class="feature water">
    <path class="icon-fill" d="M198,212 C204,222 208,228 208,232 A10,10 0 0 1 188,232 C188,228 192,222 198,212 Z"/>
    <path class="icon-fill" d="M213,204 C216,209 218,212 218,214 A5,5 0 0 1 208,214 C208,212 210,209 213,204 Z"/>
    <path class="icon-line" d="M172,242 L222,242 M176,234 L184,234"/>
    <text class="feature-label" x="197" y="267" font-size="16.5" text-anchor="middle">Water resistant</text>
  </g>
  <g class="feature clean">
    <rect class="icon-fill" x="308" y="216" width="30" height="28" rx="9"/>
    <path class="icon-line" d="M300,214 L300,222 M296,218 L304,218 M314,200 L314,206 M311,203 L317,203"/>
    <text class="feature-label" x="321" y="267" font-size="16.5" text-anchor="middle">Easy to clean</text>
  </g>

  <circle cx="742" cy="165" r="34" fill="none" stroke="var(--white)" stroke-width="3"/>
  <path class="icon-fill" d="M718,164 L766,164 L762,178 Q760,184 752,184 L732,184 Q724,184 722,178 Z"/>
  <path class="icon-line" d="M726,184 L724,189 M758,184 L760,189 M730,164 L730,148 Q730,142 736,142 L742,142 M742,142 L742,150"/>
  <text class="room-label" x="738" y="220" font-size="16" text-anchor="middle">Ideal for Bathrooms</text>
  <text class="room-label" x="738" y="240" font-size="16" text-anchor="middle">and Kitchens</text>

  <text class="use-label" x="637" y="273" font-size="22" text-anchor="middle">Suitable for general domestic use</text>

  <rect x="1160" y="176" width="56" height="56" fill="var(--brown)"/>
  <text class="brand-name" x="1250" y="216" font-size="60">CORVELLA</text>
  <text class="brand-tagline" x="1252" y="238" font-size="15">Quality home flooring</text>
</svg>
</body>
</html>
```